Marlow Realty Real Estate Brokerage Recruiting Flyer

We are a real estate brokerage looking to hire more real estate agents. We need to list everything we have to offer as a company so real estate agents will join our company. this is our company website: www.Marlowrealty.example .

100% COMMISSION NO MONTHLY FEE
$450 Flat Transaction FEE

What We Offer:
24/7 Office Access
Free E & O Insurance for 1st Year
Free Online CE and PLE
Free 1,000 Business Cards
Free Professional Social Media Marketing
Free Printing, Scanning, and Copies
Free Buyer and Seller Presentation Packages
Free Filquay Cloud Based Document Management Access
Access to our Internal Brokerage Forum
Company Profit Sharing!
Private Offices Available to Rent

*Lead Generation Software with over 3,000 Leads
*10 Leads to Start
* Free Personal CRM and Website
*Restrictions and Rules apply

Company Address:
4817 Amberfield Road
Suite 512
Fairfax, VA 22194
Phone: 703-555-0147
email: info@marlowrealty.example

Target Market(s)

Real Estate Agents

Industry/Entity Type

Real Estate

Colors
0555a3
ffffff

Requirements
Must have
• 100% COMMISSION NO MONTHLY FEE
$450 Flat Transaction FEE

What We Offer:
24/7 Office Access
Free Online CE and PLE
Free 1,000 Business Cards
Company Profit Sharing!

*10 Leads to Start

Company Address:
4817 Amberfield Road
Suite 512
Fairfax, VA 22194
Phone: 703-555-0147

```html
<!DOCTYPE html>
<html lang="en">
<head>
<meta charset="utf-8">
<title>Marlow Realty – Agent Recruiting Flyers</title>
<link href="https://fonts.googleapis.com/css2?family=Saira+Semi+Condensed:wght@600;700;800&family=Roboto:wght@400;500;700&display=swap" rel="stylesheet">
<style>
  :root{
    --navy:#1b3e78;
    --ice:#e8f1fb;
    --white:#ffffff;
    --canvas:#ececec;
    --ink:#1b3e78;
    --head:"Saira Semi Condensed", sans-serif;
    --body:"Roboto", sans-serif;
  }
  *{margin:0;padding:0;box-sizing:border-box}
  html,body{width:1200px;height:625px;overflow:hidden;background:var(--canvas)}
  .stage{position:relative;width:1200px;height:625px}
  .flyer{position:absolute;top:19px;width:402px;height:588px;background:var(--white);overflow:hidden;font-family:var(--body);color:var(--ink)}
  .flyer--family{left:186px}
  .flyer--house{left:608px}
  .abs{position:absolute}
  .nowrap{white-space:nowrap}

  /* ---------- family flyer ---------- */
  .hero-art{left:0;top:0;width:402px;height:205px}
  .headline-band{left:0;top:205px;width:250px;height:44px;background:var(--navy);color:var(--white);font-family:var(--head);font-weight:700;padding:4px 0 0 6px;line-height:1;white-space:nowrap;overflow:hidden}
  .headline-band .l1{font-size:12.5px}
  .headline-band .rule{height:1px;background:rgba(255,255,255,.7);margin:3px 6px 3px 0}
  .headline-band .l2{font-size:16px}
  .brand-block{left:250px;top:205px;width:130px;height:53px;display:flex;align-items:center;justify-content:center;gap:4px}
  .brand-mark{width:8px;height:8px;background:var(--navy);flex:none}
  .brand-name{font-family:var(--head);font-weight:700;font-size:11.5px;color:var(--navy);white-space:nowrap}
  .brand-edge{left:380px;top:205px;width:22px;height:53px;background:var(--navy)}
  .offer-bar{left:0;top:258px;width:250px;height:19px;background:var(--ice)}
  .offer-bar .tab{position:absolute;left:0;top:0;width:13px;height:19px;background:var(--navy)}
  .offer-bar h2{position:absolute;left:17px;top:2px;font-family:var(--body);font-weight:700;font-size:12px;color:var(--navy)}
  .tile{position:absolute;display:flex;flex-direction:column}
  .tile-photo{flex:1}
  .tile-label{height:23px;background:var(--navy);color:var(--white);font-size:6.2px;font-weight:500;line-height:1.15;text-align:center;display:flex;align-items:center;justify-content:center;padding:0 2px}
  .key-art{left:259px;top:258px;width:121px;height:100px;background:linear-gradient(135deg,#eef5fd,#dfeaf7)}
  .perk-panel{left:259px;top:358px;width:121px;height:106px;background:var(--navy);border-radius:0 0 10px 10px;color:var(--white);padding:6px 4px 0 3px}
  .perk-panel li{list-style:none;font-size:7.8px;line-height:1.25;margin-bottom:6px;padding-left:8px;position:relative}
  .perk-panel li::before{content:"*";position:absolute;left:0;top:0}
  .license-block{left:259px;top:471px;font-weight:500;color:var(--navy);line-height:1.1;white-space:nowrap}
  .license-block .lead{font-size:10px}
  .license-block .states{font-size:12px;font-weight:700}
  .foot-band{left:173px;top:513px;width:229px;height:75px;background:var(--navy);color:var(--white);padding:6px 0 0 8px}
  .foot-band h3,.house-foot h3{font-size:7.5px;font-weight:500;text-decoration:underline;margin-bottom:2px}
  .contact{font-size:7.5px;line-height:1.45;white-space:nowrap}
  .contact .row{display:flex;align-items:center;gap:4px}
  .contact svg{width:7px;height:7px;flex:none}
  .contact .indent{padding-left:11px}
  .phone-pill{position:absolute;background:var(--white);color:var(--navy);font-family:var(--head);font-weight:800;border-radius:4px;display:flex;align-items:center;justify-content:center;white-space:nowrap}
  .foot-band .phone-pill{left:122px;top:43px;width:100px;height:19px;font-size:14px}

  /* ---------- house flyer ---------- */
  .house-art{left:21px;top:19px;width:361px;height:164px}
  .house-brand{left:39px;top:19px;width:133px;height:53px;background:var(--white);display:flex;align-items:center;justify-content:center;gap:4px}
  .house-head{left:21px;top:185px;width:361px;height:64px;background:var(--navy);color:var(--white);font-family:var(--head);font-weight:700;text-align:center;padding-top:7px;line-height:1;white-space:nowrap;overflow:hidden}
  .house-head .l1{font-size:18px}
  .house-head .rule{height:1px;background:rgba(255,255,255,.7);margin:5px 10px}
  .house-head .l2{font-size:23px}
  .offer-box{left:21px;top:251px;width:361px;height:187px;border:1px solid #9fb0c9;border-top:none}
  .offer-box h2{position:absolute;left:3px;top:0;font-size:12px;font-weight:700;color:var(--navy)}
  .perk{position:absolute;width:86px;text-align:center;font-size:7px;line-height:1.3;color:#222}
  .perk svg{display:block;margin:0 auto 2px;width:20px;height:20px}
  .pill{position:absolute;height:28px;background:var(--navy);color:var(--white);border-radius:14px;font-family:var(--head);font-weight:700;font-size:8.6px;line-height:1.05;display:flex;align-items:center;white-space:nowrap}
  .pill .star{position:absolute;top:1px;width:26px;height:26px;border-radius:50%;background:var(--white);border:2px solid var(--navy);display:flex;align-items:center;justify-content:center;color:var(--navy);font-size:16px;font-family:var(--body)}
  .house-foot{left:21px;top:512px;width:361px;height:75px;background:var(--navy);color:var(--white)}
  .house-foot .addr{position:absolute;left:7px;top:6px}
  .house-foot .divider{position:absolute;left:176px;top:6px;width:1px;height:62px;background:rgba(255,255,255,.8)}
  .house-foot .lic{position:absolute;left:182px;top:7px;font-weight:500;line-height:1.1;white-space:nowrap}
  .house-foot .lic .lead{font-size:10px}
  .house-foot .lic .states{font-size:12px;font-weight:700}
  .house-foot .phone-pill{left:182px;top:40px;width:100px;height:19px;font-size:14px}
</style>
</head>
<body>
<div class="stage">

  <section class="flyer flyer--family">
    <svg class="abs hero-art" viewBox="0 0 402 205" role="img" aria-label="Photo of a smiling family of four posing together in a bright living room">
      <defs>
        <linearGradient id="roomTone" x1="0" y1="0" x2="1" y2="1">
          <stop offset="0" stop-color="#eef3f6"/>
          <stop offset=".55" stop-color="#cfdde3"/>
          <stop offset="1" stop-color="#e9e2da"/>
        </linearGradient>
      </defs>
      <rect width="402" height="205" fill="#1b3e78"/>
      <path d="M175 14 H402 V205 H0 V200 L110 40 Q128 14 175 14 Z" fill="url(#roomTone)"/>
    </svg>

    <div class="abs headline-band">
      <div class="l1">100% COMMISSION NO MONTHLY FEE</div>
      <div class="rule"></div>
      <div class="l2">$450 FLAT TRANSACTION FEE</div>
    </div>
    <div class="abs brand-block"><span class="brand-mark"></span><span class="brand-name">MARLOW REALTY</span></div>
    <div class="abs brand-edge"></div>

    <div class="abs offer-bar"><span class="tab"></span><h2>WHAT WE OFFER:</h2></div>

    <div class="tile" style="left:13px;top:277px;width:73px;height:72px"><div class="tile-photo" role="img" aria-label="Photo of agents working on laptops" style="background:linear-gradient(160deg,#c9d3dc,#7d8a98)"></div><div class="tile-label">24/7 Office Access</div></div>
    <div class="tile" style="left:92px;top:277px;width:74px;height:72px"><div class="tile-photo" role="img" aria-label="Photo of a business strategy document on a desk" style="background:linear-gradient(160deg,#d8dde2,#8a9098)"></div><div class="tile-label">Free E &amp; O Insurance for 1st Year</div></div>
    <div class="tile" style="left:173px;top:277px;width:77px;height:72px"><div class="tile-photo" role="img" aria-label="Photo of a presenter teaching a class" style="background:linear-gradient(160deg,#eef0f2,#a9aeb3)"></div><div class="tile-label">Free Online CE and PLE</div></div>

    <div class="tile" style="left:13px;top:356px;width:73px;height:72px"><div class="tile-photo" role="img" aria-label="Photo of stacked business cards" style="background:linear-gradient(160deg,#f4f5f6,#c7ccd0)"></div><div class="tile-label">Free 1,000<br>Business Cards</div></div>
    <div class="tile" style="left:92px;top:356px;width:74px;height:72px"><div class="tile-photo" role="img" aria-label="Illustration of a social media icon tree" style="background:linear-gradient(160deg,#f7e58a,#f1b94a)"></div><div class="tile-label">Free Professional Social Media Marketing</div></div>
    <div class="tile" style="left:173px;top:356px;width:77px;height:72px"><div class="tile-photo" role="img" aria-label="Photo of a printed business plan coming from a printer" style="background:linear-gradient(160deg,#eef1f4,#b7c0c9)"></div><div class="tile-label">Free Printing, Scanning, and Copies</div></div>

    <div class="tile" style="left:13px;top:435px;width:73px;height:70px"><div class="tile-photo" role="img" aria-label="Photo of a team meeting at a table" style="background:linear-gradient(160deg,#d9d4cc,#8c8f94)"></div><div class="tile-label">Free Buyer and Seller Presentation Packages</div></div>
    <div class="tile" style="left:92px;top:435px;width:74px;height:70px"><div class="tile-photo" role="img" aria-label="Illustration of a hand touching a digital cloud network" style="background:linear-gradient(160deg,#2d6fb8,#0d2447)"></div><div class="tile-label">Free Filquay Cloud Based Document</div></div>
    <div class="tile" style="left:173px;top:435px;width:77px;height:70px"><div class="tile-photo" role="img" aria-label="Photo of a calculator and financial charts" style="background:linear-gradient(160deg,#f2f3f5,#b9bfc7)"></div><div class="tile-label">Access to our Internal Brokerage Forum Company Profit Sharing!</div></div>

    <div class="tile" style="left:13px;top:512px;width:73px;height:72px"><div class="tile-photo" role="img" aria-label="Photo of cash and financial charts" style="background:linear-gradient(160deg,#e7e3d4,#9aa386)"></div><div class="tile-label">Company Profit Sharing!</div></div>
    <div class="tile" style="left:92px;top:512px;width:74px;height:72px"><div class="tile-photo" role="img" aria-label="Photo of a woman working in a private office" style="background:linear-gradient(160deg,#e3e8ea,#98a4a8)"></div><div class="tile-label">Private Offices Available to Rent</div></div>

    <div class="abs key-art" role="img" aria-label="Illustration of a hand passing house keys to a hand holding a small house"></div>
    <ul class="abs perk-panel">
      <li>Lead Generation Software with over 3,000 Leads</li>
      <li>Free Personal CRM and Website</li>
      <li>10 Leads to Start</li>
      <li>Restrictions and Rules apply</li>
    </ul>

    <div class="abs license-block">
      <div class="lead">LICENSED IN</div>
      <div class="states">D.C &nbsp;|&nbsp; MARYLAND<br>VIRGINIA</div>
    </div>

    <div class="abs foot-band">
      <h3>COMPANY ADDRESS</h3>
      <div class="contact">
        <div class="row"><svg viewBox="0 0 10 10"><path d="M1 9V4l4-3 4 3v5H6V6H4v3z" fill="#fff"/></svg>4817 Amberfield Road, Suite 512</div>
        <div class="indent">Fairfax, VA 22194</div>
        <div class="row"><svg viewBox="0 0 10 10"><circle cx="5" cy="3" r="2.2" fill="#fff"/><path d="M1 10a4 4 0 0 1 8 0z" fill="#fff"/></svg>703-555-0147</div>
        <div class="row"><svg viewBox="0 0 10 10"><rect x="0.5" y="2" width="9" height="6.5" fill="#fff"/><path d="M0.5 2l4.5 3.5L9.5 2" stroke="#1b3e78" stroke-width="1" fill="none"/></svg>info@marlowrealty.example</div>
      </div>
      <div class="phone-pill">703-555-0147</div>
    </div>
  </section>

  <section class="flyer flyer--house">
    <div class="abs house-art" role="img" aria-label="Photo of a gabled white and grey-blue house with a green lawn under a blue sky" style="background:linear-gradient(180deg,#4f95d8 0%,#a9cdea 45%,#cfd6d6 58%,#6f9a4a 78%,#3f7a2a 100%)"></div>
    <div class="abs house-brand"><span class="brand-mark"></span><span class="brand-name">MARLOW REALTY</span></div>

    <div class="abs house-head">
      <div class="l1">100% COMMISSION NO MONTHLY FEE</div>
      <div class="rule"></div>
      <div class="l2">$450 FLAT TRANSACTION FEE</div>
    </div>

    <div class="abs offer-box">
      <h2>WHAT WE OFFER:</h2>

      <div class="perk" style="left:2px;top:18px"><svg viewBox="0 0 20 20"><circle cx="10" cy="10" r="8" fill="none" stroke="#1b3e78" stroke-width="2"/><text x="10" y="12.6" text-anchor="middle" font-size="7" font-weight="700" fill="#1b3e78" font-family="Roboto, sans-serif">24</text></svg>24/7 Office Access</div>
      <div class="perk" style="left:92px;top:18px"><svg viewBox="0 0 20 20"><rect x="3" y="1" width="11" height="15" rx="1" fill="#1b3e78"/><path d="M5 5h7M5 8h7M5 11h4" stroke="#fff" stroke-width="1.2"/><circle cx="14.5" cy="14.5" r="4.5" fill="#1b3e78" stroke="#fff"/><path d="M12.5 14.5l1.5 1.5 2.5-3" stroke="#fff" stroke-width="1.2" fill="none"/></svg>Free E &amp; O Insurance for 1st Year</div>
      <div class="perk" style="left:182px;top:18px"><svg viewBox="0 0 20 20"><rect x="8" y="1" width="11" height="9" fill="none" stroke="#1b3e78" stroke-width="1.6"/><circle cx="4.5" cy="5" r="2.5" fill="#1b3e78"/><path d="M1 19v-7a3 3 0 0 1 6 0v7zM7 11l4-3" stroke="#1b3e78" stroke-width="1.6" fill="#1b3e78"/></svg>Free Online CE and PLE</div>
      <div class="perk" style="left:272px;top:18px"><svg viewBox="0 0 20 20"><rect x="2" y="6" width="16" height="11" rx="1.5" fill="#1b3e78"/><circle cx="6.5" cy="10.5" r="2" fill="#fff"/><path d="M10 10h6M10 13h6" stroke="#fff" stroke-width="1.2"/><path d="M5 6l8-4 2 4" fill="#1b3e78"/></svg>Free 1,000 Business Cards</div>

      <div class="perk" style="left:2px;top:73px"><svg viewBox="0 0 20 20"><path d="M2 8h4l8-5v14l-8-5H2z" fill="#1b3e78"/><circle cx="16" cy="4" r="1.6" fill="#1b3e78"/><circle cx="17" cy="10" r="1.6" fill="#1b3e78"/><circle cx="16" cy="16" r="1.6" fill="#1b3e78"/></svg>Free Professional Social Media Marketing</div>
      <div class="perk" style="left:92px;top:73px"><svg viewBox="0 0 20 20"><rect x="5" y="2" width="10" height="5" fill="#1b3e78"/><rect x="1" y="7" width="18" height="8" rx="1.5" fill="#1b3e78"/><rect x="5" y="12" width="10" height="6" fill="#fff" stroke="#1b3e78" stroke-width="1.4"/></svg>Free Printing, Scanning, and Copies</div>
      <div class="perk" style="left:182px;top:73px"><svg viewBox="0 0 20 20"><path d="M2 5l7-3 7 3v9l-7 4-7-4z" fill="#1b3e78"/><path d="M2 5l7 3 7-3M9 8v10" stroke="#fff" stroke-width="1"/><rect x="14" y="10" width="5" height="8" fill="#1b3e78" stroke="#fff" stroke-width=".8"/></svg>Free Buyer and Seller Presentation Packages</div>
      <div class="perk" style="left:272px;top:73px"><svg viewBox="0 0 20 20"><path d="M5 9a4 4 0 0 1 1-7 5 5 0 0 1 9 2 3 3 0 0 1 0 5z" fill="#1b3e78"/><path d="M10 9v4M4 13h12M4 13v3M10 13v3M16 13v3" stroke="#1b3e78" stroke-width="1.5"/><rect x="2" y="16" width="4" height="3" fill="#1b3e78"/><rect x="8" y="16" width="4" height="3" fill="#1b3e78"/><rect x="14" y="16" width="4" height="3" fill="#1b3e78"/></svg>Free Filquay Cloud Based Document Management Access</div>

      <div class="perk" style="left:45px;top:130px"><svg viewBox="0 0 20 20"><rect x="3" y="1" width="14" height="6" rx="1.5" fill="#1b3e78"/><circle cx="10" cy="10.5" r="2.2" fill="#1b3e78"/><path d="M6 19a4 4 0 0 1 8 0z" fill="#1b3e78"/><circle cx="3.5" cy="11" r="1.8" fill="#1b3e78"/><circle cx="16.5" cy="11" r="1.8" fill="#1b3e78"/><path d="M0 18a3.5 3.5 0 0 1 7 0zM13 18a3.5 3.5 0 0 1 7 0z" fill="#1b3e78"/></svg>Access to our Internal Brokerage Forum Company Profit Sharing!</div>
      <div class="perk" style="left:140px;top:130px"><svg viewBox="0 0 20 20"><circle cx="13" cy="5" r="4" fill="#1b3e78"/><text x="13" y="7.3" text-anchor="middle" font-size="6" font-weight="700" fill="#fff" font-family="Roboto, sans-serif">$</text><path d="M1 13h4l4 2h5l5-3-1 4-7 3H6l-5-2z" fill="#1b3e78"/></svg>Company Profit Shar-<br>ing!</div>
      <div class="perk" style="left:230px;top:130px"><svg viewBox="0 0 20 20"><rect x="2" y="9" width="4" height="10" fill="#1b3e78"/><rect x="7" y="3" width="5" height="16" fill="#1b3e78"/><rect x="13" y="7" width="4" height="12" fill="#1b3e78"/><circle cx="16" cy="4" r="3" fill="#1b3e78"/></svg>Private Offices Availa-<br>ble to Rent</div>
    </div>

    <div class="pill" style="left:21px;top:442px;width:177px;padding-left:34px"><span class="star" style="left:1px">*</span>LEAD GENERATION SOFTWARE<br>WITH OVER 3,000 LEADS</div>
    <div class="pill" style="left:205px;top:442px;width:177px;padding-left:34px;font-size:9.5px"><span class="star" style="left:1px">*</span>FREE PERSONAL CRM<br>AND WEBSITE</div>
    <div class="pill" style="left:21px;top:479px;width:177px;justify-content:center;padding-right:28px;font-size:10.5px">10 LEADS TO START<span class="star" style="right:1px">*</span></div>
    <div class="pill" style="left:205px;top:479px;width:177px;justify-content:flex-end;padding-right:34px;text-align:right;font-size:9.5px">RESTRICTIONS AND<br>RULES APPLY<span class="star" style="right:1px">*</span></div>

    <div class="abs house-foot">
      <div class="addr">
        <h3>COMPANY ADDRESS</h3>
        <div class="contact">
          <div class="row"><svg viewBox="0 0 10 10"><path d="M1 9V4l4-3 4 3v5H6V6H4v3z" fill="#fff"/></svg>4817 Amberfield Road, Suite 512</div>
          <div class="indent">Fairfax, VA 22194</div>
          <div class="row"><svg viewBox="0 0 10 10"><circle cx="5" cy="3" r="2.2" fill="#fff"/><path d="M1 10a4 4 0 0 1 8 0z" fill="#fff"/></svg>703-555-0147</div>
          <div class="row"><svg viewBox="0 0 10 10"><rect x="0.5" y="2" width="9" height="6.5" fill="#fff"/><path d="M0.5 2l4.5 3.5L9.5 2" stroke="#1b3e78" stroke-width="1" fill="none"/></svg>info@marlowrealty.example</div>
        </div>
      </div>
      <div class="divider"></div>
      <div class="lic">
        <div class="lead">LICENSED IN</div>
        <div class="states">D.C &nbsp;|&nbsp; MARYLAND | VIRGINIA</div>
      </div>
      <div class="phone-pill">703-555-0147</div>
    </div>
  </section>

</div>
</body>
</html>
```